Brightmoor Business Solutions

I need a business card design with logo for my business and management consultancy business. I am based in Singapore and I provide (i) accounting / bookkeeping services; (ii) management and business consultancy solutions; (iii) tax advisory and consultancy; and (iv) risk management and corporate governance. I want the design to be bold and outstanding yet doesn't give the impression that I take unnecessary risks.

Reason: To the designers who have gotten messages from me, I'm still waiting for some changes to be made.

Target Market(s)

Small to large enterprises which are willing to pay value for money and not necessarily the cheapest

Industry/Entity Type

Accounting

Contact Information for Business Card

Name, email address and mobile no.

Requirements
Must have
• If possible, could you incorporate the Sigma symbol as the E for Brightmoor or the Equals sign to show that the business relates to finance / financials and that I provide solutions which may it easy for my clients.
Should not have
• Black / dark backgrounds

```html
<!DOCTYPE html>
<html lang="en">
<head>
<meta charset="utf-8">
<title>Brightmoor Business Solutions – Business Card</title>
<link rel="stylesheet" href="https://fonts.googleapis.com/css2?family=Arimo:wght@400;700&display=swap">
<style>
  :root {
    --backdrop: #a9a9ab;
    --card: #ffffff;
    --ink: #1f1f1f;
    --band: #3b3b3b;
    --band-text: #e6e6e6;
    --rule: #9a9a9a;
  }
  * { box-sizing: border-box; margin: 0; padding: 0; }
  html, body {
    width: 1200px;
    height: 800px;
    overflow: hidden;
  }
  body {
    background: var(--backdrop);
    font-family: "Arimo", Arial, sans-serif;
    color: var(--ink);
    position: relative;
  }
  .business-card {
    position: absolute;
    left: 390px;
    top: 70px;
    width: 420px;
    height: 660px;
    background: var(--card);
    box-shadow: 0 6px 18px rgba(0,0,0,0.25);
  }
  .brand {
    position: absolute;
    left: 40px;
    top: 108px;
    display: flex;
    align-items: center;
    gap: 14px;
  }
  .brand-mark {
    width: 38px;
    height: 38px;
    background: var(--ink);
    flex: none;
  }
  .brand-name {
    font-weight: 700;
    font-size: 42px;
    line-height: 1;
    letter-spacing: -0.5px;
    color: var(--ink);
  }
  .brand-tagline {
    position: absolute;
    left: 92px;
    top: 156px;
    font-weight: 700;
    font-size: 17px;
    color: var(--ink);
  }
  .contact {
    position: absolute;
    left: 36px;
    top: 276px;
  }
  .contact-name {
    font-size: 29px;
    font-weight: 400;
    letter-spacing: 0.5px;
    margin-bottom: 14px;
  }
  .contact-line {
    font-size: 17px;
    line-height: 1.45;
  }
  .rule {
    position: absolute;
    left: 0;
    width: 100%;
    height: 1px;
    background: var(--rule);
  }
  .rule-top { top: 414px; }
  .rule-bottom { top: 570px; }
  .services-band {
    position: absolute;
    left: 0;
    top: 424px;
    width: 100%;
    height: 136px;
    background: var(--band);
    padding: 26px 22px 0;
    list-style: none;
  }
  .services-band li {
    color: var(--band-text);
    font-size: 15px;
    line-height: 1.52;
  }
</style>
</head>
<body>
  <article class="business-card">
    <div class="brand">
      <span class="brand-mark"></span>
      <span class="brand-name">Brightmoor</span>
    </div>
    <div class="brand-tagline">Business Solutions</div>

    <section class="contact">
      <h1 class="contact-name">DANA WHITFIELD</h1>
      <p class="contact-line">M: 123 XXX XXXX</p>
      <p class="contact-line">E: dana@brightmoorsolutions.com</p>
    </section>

    <div class="rule rule-top"></div>
    <ul class="services-band">
      <li>- accounting / bookkeeping services</li>
      <li>- management and business consultancy solutions</li>
      <li>- tax advisory and consultancy</li>
      <li>- risk management and corporate governance</li>
    </ul>
    <div class="rule rule-bottom"></div>
  </article>
</body>
</html>
```